Gold Ridge Workwear Web Design Project

New uploiad DESIGN 2 and DESIGN 3. These are examples of how we want to setup up our secondary pages. Only for layout purposes though. There design is a little to grey for us.
Limit blue colours to three (as per our logo). Other than blue, white should be used. We like to stay away from other colours, especially grey.
Based on the initial concent of our web site, I only like a few elements. These are:
- Header
- Mono coloured logos for brands, which then come to full colour when scrolled across The main brands we want used as examples are CORVANE / STROLIK / OPTARUN / PELTO / DEL MORVAN / FENDLE / SAFEMARK / GTK (Guardline Toolkit Kitting) / Trade Range / Feel free not to use all, depending on how much room you have to work with. Can have a slide with arrow as to see more.
Layout needs to be clean, simple and not confusing. It needs to be of corporate style, since we are a business to business company and not a consumer one. Our brand is an Australian icon and this web site design needs to reflect this. Our main clientelle is Mining, Construction, Transport, Oil & Gas, although our motto is Gear for all, Gear Gold Ridge which is to give the impression that we deal with all and everyone. We can cater to the needs of any business.
Attached is our site map / menu structure. The main titles will go across ways underneath the main header. Then a drop down menu of sorts will show the other titles one down. Any third level menus are only to be links in the pages of second level. We have highlighted featured menu subjects that we think could do with another link on the homepage also to highlight subject. Arrows down on the top level menu is to indicate then menu drops down. I do like this - open to suggestions.
Quick Quote and Industry Partner should be featured links in the main page, without being in the header menu.
Industry partner section would then relate back to the Industry Links - almost being like a header page for the rest of the Industries mentioned under the header bar.
BRANDS would have all the images of Brand under, with a possible small blurb about each one. There would be a left hand column with a menu of sorts
Industry would be set out similar with the left hand column menu, would have a few paragraphs about the industry and how we represent them through workwear, then with three rows across and three to four rows down of images which would be a small showing of what type of uniforms are on offer. No text is needed. Just want them to look clean.
Possible stamp like image - saying: THE GOLD RIDGE DIFFERENCE on the main page.
Socia Media links. Being a business to business company, ProLinker is an important social media link to have. Not so important, but still necessary is Friendspace and Chirpline. VIDTUBA.
Please keep in mind this site is to be an information site only. It's not an ecommerce site, so the web site will show a few images as examples, but nothing too specific about each garment, just an overview as such. There will be a seperate web site setup for a client portal for e-commerce side of things. A Login link and Register link on the main page are required for this. Also a VISIT THE GOLD RIDGE STORE link.
Business to Business - not consumer

```html
<!DOCTYPE html>
<html lang="en">
<head>
<meta charset="utf-8">
<title>Gold Ridge Workwear</title>
<link rel="stylesheet" href="https://fonts.googleapis.com/css2?family=Tinos:wght@700&family=Open+Sans:wght@400;600;700&family=Arimo:wght@400&display=swap">
<style>
  :root {
    --ink: #000000;
    --paper: #ffffff;
    --blue-deep: #1f3f78;
    --blue-mid: #2f5fa8;
    --blue-light: #7fa6dc;
    --bar: rgba(40, 40, 40, 0.88);
    --coat-white: #e4e4e4;
    --coat-grey: #c6c6c6;
    --scrub: #6f9fe0;
    --scrub-shade: #5a88cc;
    --rule: #555555;
  }
  * { margin: 0; padding: 0; box-sizing: border-box; }
  html, body { width: 1152px; height: 1200px; overflow: hidden; background: var(--paper); }
  .page { position: relative; width: 1152px; height: 1200px; font-family: "Open Sans", sans-serif; color: var(--ink); }

  .brand-mark { position: absolute; left: 10px; top: 22px; display: flex; align-items: center; gap: 14px; }
  .brand-mark .square { width: 76px; height: 76px; background: var(--ink); }
  .brand-mark .name { font-family: "Tinos", serif; font-weight: 700; font-size: 46px; line-height: 1; color: var(--ink); }
  .brand-mark .name span { display: block; font-size: 27px; letter-spacing: 7.5px; margin-top: 6px; }

  .stamp { position: absolute; left: 462px; top: 29px; width: 676px; height: 79px; border: 4px solid var(--ink); border-radius: 12px; display: flex; align-items: center; justify-content: center; }
  .stamp::after { content: ""; position: absolute; inset: 4px; border: 1.5px solid var(--ink); border-radius: 8px; }
  .stamp p { font-family: "Tinos", serif; font-weight: 700; font-size: 39px; letter-spacing: 1px; }

  .main-nav { position: absolute; left: 0; top: 133px; width: 1152px; height: 53px; background: var(--ink); }
  .main-nav::before { content: ""; position: absolute; left: 46px; top: 0; border-left: 9px solid transparent; border-right: 9px solid transparent; border-top: 10px solid var(--paper); }
  .main-nav a { position: absolute; top: 16px; font-family: "Tinos", serif; font-weight: 700; font-size: 18px; color: var(--paper); text-decoration: none; }

  .hero { position: absolute; left: 0; top: 186px; width: 1152px; height: 550px; }
  .hero-photo { position: absolute; inset: 0;
    background:
      linear-gradient(180deg, rgba(255,255,255,0.12) 0%, rgba(0,0,0,0) 40%, rgba(0,0,0,0.08) 100%),
      linear-gradient(90deg, var(--coat-grey) 0%, var(--coat-white) 14%, var(--coat-grey) 30%, var(--coat-white) 44%, var(--coat-white) 58%, var(--scrub) 64%, var(--scrub-shade) 76%, var(--scrub) 86%, var(--blue-light) 100%); }
  .hero-caption { position: absolute; left: 0; top: 435px; width: 1152px; height: 108px; background: var(--bar); color: var(--paper); }
  .hero-caption h2 { position: absolute; left: 38px; top: 14px; font-weight: 600; font-size: 27px; }
  .hero-caption p { position: absolute; left: 40px; top: 58px; width: 520px; font-family: "Arimo", sans-serif; font-size: 14px; line-height: 18px; }
  .thumb { position: absolute; top: 15px; height: 86px; background: var(--paper); padding: 10px; }
  .thumb div { width: 100%; height: 100%; }
  .hero-next { position: absolute; right: 35px; top: 42px; text-align: right; }
  .hero-next strong { display: block; font-weight: 600; font-size: 20px; }
  .hero-next a { font-family: "Arimo", sans-serif; font-size: 14px; color: var(--paper); text-decoration: underline; }

  .slide-dots { position: absolute; top: 744px; left: 902px; display: flex; gap: 18px; }
  .slide-dots span { width: 24px; height: 24px; border-radius: 50%; background: var(--ink); }
  .slide-dots span.active { background: var(--blue-mid); }

  .brand-strip { position: absolute; left: 31px; top: 808px; width: 1083px; height: 127px; background: var(--ink); }
  .brand-strip-shadow { position: absolute; left: 0; top: 935px; width: 1152px; height: 36px;
    background:
      radial-gradient(ellipse 190px 30px at 160px 0, rgba(31,63,120,0.85) 0%, rgba(31,63,120,0) 100%),
      radial-gradient(ellipse 190px 30px at 990px 0, rgba(31,63,120,0.85) 0%, rgba(31,63,120,0) 100%); }
  .brand-strip .arrow { position: absolute; top: 44px; }
  .brand-name { position: absolute; top: 40px; display: flex; align-items: center; gap: 10px; font-weight: 700; font-size: 36px; line-height: 46px; color: var(--paper); letter-spacing: -0.5px; }
  .brand-name i { width: 24px; height: 24px; background: var(--paper); }

  .site-footer { position: absolute; left: 0; top: 1001px; width: 1152px; height: 199px; background: var(--ink); border-top: 2px solid var(--rule); color: var(--paper); }
  .social { position: absolute; top: 30px; left: 0; width: 100%; display: flex; justify-content: center; gap: 16px; font-family: "Arimo", sans-serif; font-size: 12px; }
  .social a { display: flex; align-items: center; gap: 5px; color: var(--paper); text-decoration: none; }
  .social a i { width: 22px; height: 22px; background: var(--paper); }
  .rule { position: absolute; top: 78px; left: 12px; width: 1128px; border-top: 1px dotted #aaa; }
  .footer-nav { position: absolute; top: 95px; width: 100%; text-align: center; font-family: "Arimo", sans-serif; font-size: 14px; }
  .footer-nav a { color: var(--paper); text-decoration: none; }
  .footer-nav .sep { margin: 0 7px; }
  .copyright { position: absolute; top: 119px; width: 100%; text-align: center; font-family: "Arimo", sans-serif; font-size: 12px; }
</style>
</head>
<body>
<div class="page">
  <header>
    <div class="brand-mark">
      <div class="square"></div>
      <div class="name">GOLD RIDGE<span>WORKWEAR</span></div>
    </div>
    <div class="stamp"><p>THE GOLD RIDGE DIFFERENCE</p></div>
  </header>

  <nav class="main-nav">
    <a href="#" style="left:32px">HOME</a>
    <a href="#" style="left:160px">PRODUCTS</a>
    <a href="#" style="left:330px">INDUSTRIES</a>
    <a href="#" style="left:515px">CATALOGUES</a>
    <a href="#" style="left:708px">MEDIA</a>
    <a href="#" style="left:842px">ABOUT US</a>
    <a href="#" style="left:1004px">CONTACT</a>
  </nav>

  <section class="hero">
    <div class="hero-photo" role="img" aria-label="Photo of a healthcare team: doctors in white coats on the left, nurses in blue scrubs and caps on the right"></div>
    <div class="hero-caption">
      <h2>HEALTH CARE</h2>
      <p>I'm a paragraph. Click here to add your own text and edit me. I'm a great place for you to tell a story and let your users know a little more about you.</p>
      <div class="thumb" style="left:580px;width:87px"><div role="img" aria-label="Blue healthcare tunic" style="background:#4fa3d8"></div></div>
      <div class="thumb" style="left:674px;width:79px"><div role="img" aria-label="Pink healthcare tunic" style="background:#f1d3e0"></div></div>
      <div class="thumb" style="left:759px;width:77px"><div role="img" aria-label="Green scrub set" style="background:#1fa48a"></div></div>
      <div class="hero-next"><strong>OIL &amp; GAS</strong><a href="#">next ►</a></div>
    </div>
  </section>

  <div class="slide-dots"><span class="active"></span><span></span><span></span><span></span><span></span><span></span></div>

  <section class="brand-strip">
    <svg class="arrow" style="left:14px" width="26" height="40" viewBox="0 0 26 40"><polygon points="26,0 26,40 0,20" fill="#fff"/></svg>
    <span class="brand-name" style="left:66px"><i></i>CORVANE</span>
    <span class="brand-name" style="left:300px">STROLIK</span>
    <span class="brand-name" style="left:548px">OPTARUN</span>
    <span class="brand-name" style="left:820px">PELTO</span>
    <svg class="arrow" style="right:23px" width="26" height="40" viewBox="0 0 26 40"><polygon points="0,0 0,40 26,20" fill="#fff"/></svg>
  </section>
  <div class="brand-strip-shadow"></div>

  <footer class="site-footer">
    <div class="social">
      <a href="#"><i></i>Chirpline</a>
      <a href="#"><i></i>Friendspace</a>
      <a href="#"><i></i>ProLinker</a>
      <a href="#"><i></i>Circlecast</a>
      <a href="#"><i></i>VIDTUBA</a>
    </div>
    <div class="rule"></div>
    <nav class="footer-nav">
      <a href="#">HOME</a><span class="sep">·</span><a href="#">PRODUCTS</a><span class="sep">·</span><a href="#">INDUSTRIES</a><span class="sep">·</span><a href="#">CATALOGUES</a><span class="sep">·</span><a href="#">MEDIA</a><span class="sep">·</span><a href="#">ABOUT US</a><span class="sep">·</span><a href="#">CONTACT</a>
    </nav>
    <p class="copyright">© Copyright 2013 GoldRidge. All Rights Reserved</p>
  </footer>
</div>
</body>
</html>
```